RKW Automotive needs a catchy banner design

We need a design for a banner to be displayed on the fence in the outfield of a baseball stadium to show off our company and have people interested in what we do. We need something catchy that's going to attract people to look over at our banner.
We are a
Reliable Auto Care & Repair Garage
Tires - Service - Repair - Diesel
We are in a Town called Maple-Hollow
(555)314-2096 we would like the phone number to be a descent size so when you are in the stands you can read it.
I have attached what we came up with but like I said we need it to pop more and make the viewer that's looking at it want to look us up.
The Banner size is 24ft long and 10ft tall

```html
<!DOCTYPE html>
<html lang="en">
<head>
<meta charset="UTF-8">
<title>RKW Automotive – Outfield Banner</title>
<link rel="stylesheet" href="https://fonts.googleapis.com/css2?family=Exo+2:ital,wght@1,900&family=Saira+Condensed:wght@700;800&family=Krona+One&display=swap">
<style>
  :root {
    --page-bg: #e4e4e4;
    --banner-bg: #0b0b0c;
    --banner-bg-2: #17181a;
    --brand-blue: #2893ff;
    --silver-light: #ffffff;
    --silver-mid: #c9c9c9;
    --silver-dark: #8d8d8d;
    --white: #ffffff;
  }
  * { box-sizing: border-box; margin: 0; padding: 0; }
  html, body {
    width: 1200px;
    height: 720px;
    overflow: hidden;
    background: var(--page-bg);
  }
  .banner {
    position: absolute;
    left: 20px;
    top: 119px;
    width: 1160px;
    height: 482px;
    background: linear-gradient(135deg, var(--banner-bg-2), var(--banner-bg) 60%);
    overflow: hidden;
  }
  .brand-name {
    position: absolute;
    left: 64px;
    top: 56px;
    width: 414px;
    height: 290px;
    display: flex;
    flex-direction: column;
    align-items: center;
    justify-content: center;
    font-family: "Saira Condensed", sans-serif;
    font-weight: 800;
    color: var(--brand-blue);
    line-height: 0.95;
    text-align: center;
  }
  .brand-name .brand-initials { font-size: 128px; letter-spacing: 4px; }
  .brand-name .brand-word { font-size: 56px; letter-spacing: 3px; }
  .headline {
    position: absolute;
    left: 527px;
    top: 44px;
    width: 572px;
    text-align: center;
    font-family: "Exo 2", sans-serif;
    font-style: italic;
    font-weight: 900;
  }
  .headline-main {
    display: block;
    font-size: 80px;
    line-height: 1;
    letter-spacing: -2px;
    background: linear-gradient(180deg, var(--silver-light) 0%, var(--silver-mid) 50%, var(--silver-dark) 100%);
    -webkit-background-clip: text;
    background-clip: text;
    color: transparent;
  }
  .headline-sub {
    display: block;
    margin-top: 4px;
    font-size: 38px;
    line-height: 1;
    letter-spacing: -0.5px;
    color: var(--brand-blue);
    white-space: nowrap;
  }
  .contact-box {
    position: absolute;
    left: 556px;
    top: 196px;
    width: 516px;
    height: 147px;
    border: 2px solid var(--brand-blue);
    border-radius: 6px;
    overflow: hidden;
    background: #000;
  }
  .contact-town {
    height: 66px;
    display: flex;
    align-items: center;
    justify-content: center;
    font-family: "Krona One", sans-serif;
    font-size: 29px;
    color: var(--white);
    letter-spacing: 0.5px;
  }
  .contact-phone {
    height: 81px;
    background: var(--brand-blue);
    display: flex;
    align-items: center;
    justify-content: center;
    gap: 16px;
    font-family: "Saira Condensed", sans-serif;
    font-weight: 800;
    font-size: 62px;
    color: var(--white);
    letter-spacing: 0.5px;
  }
  .contact-phone svg { width: 60px; height: 60px; flex: none; }
  .services {
    position: absolute;
    left: 64px;
    top: 380px;
    width: 1033px;
    display: flex;
    justify-content: space-between;
    list-style: none;
    font-family: "Saira Condensed", sans-serif;
    font-weight: 800;
    font-size: 62px;
    line-height: 1;
  }
  .service { display: flex; align-items: center; gap: 4px; }
  .service-chevron { width: 34px; height: 42px; flex: none; }
  .service-label {
    letter-spacing: 1px;
    background: linear-gradient(180deg, var(--silver-light) 0%, var(--silver-mid) 55%, var(--silver-dark) 100%);
    -webkit-background-clip: text;
    background-clip: text;
    color: transparent;
  }
</style>
</head>
<body>
  <main class="banner">
    <div class="brand-name">
      <span class="brand-initials">RKW</span>
      <span class="brand-word">Automotive</span>
    </div>

    <h1 class="headline">
      <span class="headline-main">Reliable</span>
      <span class="headline-sub">Auto Care &amp; Repair Garage</span>
    </h1>

    <div class="contact-box">
      <div class="contact-town">MAPLE-HOLLOW</div>
      <div class="contact-phone">
        <svg viewBox="0 0 60 60" aria-hidden="true">
          <circle cx="30" cy="30" r="27" fill="none" stroke="#fff" stroke-width="5"/>
          <circle cx="30" cy="30" r="19" fill="#fff"/>
          <path d="M23 19c2-1 3 0 4 2l1 4c0 1-1 2-2 2 1 3 3 5 6 7 0-1 1-2 2-2l4 1c2 1 3 2 2 4-1 2-3 3-5 3-8-2-13-8-14-16 0-2 1-4 2-5z" fill="var(--brand-blue)"/>
        </svg>
        <span>(555)314-2096</span>
      </div>
    </div>

    <ul class="services">
      <li class="service">
        <svg class="service-chevron" viewBox="0 0 34 42" aria-hidden="true">
          <polygon points="0,0 9,0 19,21 9,42 0,42 10,21" fill="var(--brand-blue)"/>
          <polygon points="13,0 22,0 32,21 22,42 13,42 23,21" fill="var(--silver-mid)"/>
        </svg>
        <span class="service-label">TIRES</span>
      </li>
      <li class="service">
        <svg class="service-chevron" viewBox="0 0 34 42" aria-hidden="true">
          <polygon points="0,0 9,0 19,21 9,42 0,42 10,21" fill="var(--brand-blue)"/>
          <polygon points="13,0 22,0 32,21 22,42 13,42 23,21" fill="var(--silver-mid)"/>
        </svg>
        <span class="service-label">SERVICE</span>
      </li>
      <li class="service">
        <svg class="service-chevron" viewBox="0 0 34 42" aria-hidden="true">
          <polygon points="0,0 9,0 19,21 9,42 0,42 10,21" fill="var(--brand-blue)"/>
          <polygon points="13,0 22,0 32,21 22,42 13,42 23,21" fill="var(--silver-mid)"/>
        </svg>
        <span class="service-label">REPAIR</span>
      </li>
      <li class="service">
        <svg class="service-chevron" viewBox="0 0 34 42" aria-hidden="true">
          <polygon points="0,0 9,0 19,21 9,42 0,42 10,21" fill="var(--brand-blue)"/>
          <polygon points="13,0 22,0 32,21 22,42 13,42 23,21" fill="var(--silver-mid)"/>
        </svg>
        <span class="service-label">DIESEL</span>
      </li>
    </ul>
  </main>
</body>
</html>
```